RESIDENCE VALBRUNETTE

The CORVALIS Immobilier company exclusively offers apartments for sale under a tax exemption law (BRESSAUTINIÉ) in CAMBRAI, 92 apartments are available, fully renovated with balcony, terrace, elevator, in a former military residence known to the city.
We want to make a book to give to our customers.

```html
<!DOCTYPE html>
<html lang="fr">
<head>
<meta charset="utf-8">
<title>Résidence Valbrunette – Cambrai</title>
<link href="https://fonts.googleapis.com/css2?family=PT+Sans:wght@400;700&family=PT+Sans+Narrow:wght@400;700&display=swap" rel="stylesheet">
<style>
  :root{
    --backdrop:#e6e6e6;
    --paper:#f7f7f6;
    --ink:#222222;
    --title-box:#dcc6a4;
    --gold:#a9742c;
    --frame:#d9c8a8;
    --gutter-shade:rgba(0,0,0,0.10);
  }
  *{box-sizing:border-box;margin:0;padding:0}
  html,body{width:1200px;height:800px;overflow:hidden;background:var(--backdrop)}
  .spread{
    position:absolute;left:20px;top:188px;width:1160px;height:424px;
    display:flex;box-shadow:0 6px 18px rgba(0,0,0,0.18);
  }
  .page{position:relative;width:580px;height:424px;overflow:hidden}
  .page--text{background:var(--paper)}
  .page--text::after{
    content:"";position:absolute;top:0;right:0;width:36px;height:100%;
    background:linear-gradient(to right,rgba(0,0,0,0),var(--gutter-shade));
    pointer-events:none;
  }
  .title-box{
    position:absolute;left:27px;top:0;width:126px;height:98px;
    background:var(--title-box);display:flex;align-items:flex-end;
    padding:0 0 27px 9px;
  }
  .title-box h1{
    font-family:"PT Sans",sans-serif;font-weight:400;font-size:15px;
    color:var(--gold);letter-spacing:0.3px;line-height:1;
  }
  .column{
    position:absolute;font-family:"PT Sans Narrow",sans-serif;font-size:7.3px;
    line-height:10.4px;color:var(--ink);text-align:justify;hyphens:auto;
  }
  .column p{text-indent:6px;margin-bottom:3px}
  .column p.cont{text-indent:0}
  .col-1{left:27px;top:107px;width:126px}
  .col-2{left:158px;top:107px;width:128px}
  .col-3{left:297px;top:177px;width:128px}
  .col-4{left:431px;top:177px;width:128px}
  .framed-view{
    position:absolute;border:3px solid var(--frame);
    box-shadow:1px 2px 4px rgba(0,0,0,0.25);
  }
  .view-courtyard{
    left:299px;top:20px;width:253px;height:154px;
    background:linear-gradient(180deg,#8fb4d8 0%,#b9735c 32%,#7d9a5a 60%,#6f9a4c 100%);
  }
  .view-facade{
    left:26px;top:250px;width:260px;height:152px;
    background:linear-gradient(180deg,#9dbfe0 0%,#b4634e 40%,#c7b8ab 70%,#6b6b6b 100%);
  }
  .view-entrance{
    position:absolute;inset:0;
    background:linear-gradient(120deg,#8db6dc 0%,#e6e6e2 30%,#a9583f 55%,#5f8a46 80%,#8d8d8d 100%);
  }
  .brand-tile{
    position:absolute;left:476px;top:333px;width:81px;height:91px;background:#ffffff;
    display:flex;flex-direction:column;align-items:center;justify-content:center;gap:6px;
  }
  .brand-tile .mark{width:14px;height:14px;background:var(--gold)}
  .brand-tile .name{
    font-family:"PT Sans",sans-serif;font-weight:400;font-size:7.5px;
    color:var(--gold);text-align:center;line-height:9px;
  }
</style>
</head>
<body>
  <div class="spread">
    <section class="page page--text">
      <div class="title-box"><h1>CAMBRAI</h1></div>

      <div class="column col-1">
        <p>Est une commune française, historiquement Capitale du Cambrésis, située dans le Département du Nord, dont elle est aujourd'hui l'une des sous-préfectures, en région Hauts-de-France. Cambrai est une ville moyenne qui compte 32 501 habitants au recensement de 2018 ; elle est au coeur de l'Unité urbaine de Cambrai qui, avec 46 772 habitants (2018), la place au 7e rang départemental. Son aire d'attraction, plus étendue, rassemble 94 576 habitants</p>
      </div>

      <div class="column col-2">
        <p class="cont">(2018). Avec Lille et les villes de l'ancien bassin minier du Nord-Pas-de-Calais, elle participe aussi à un ensemble métropolitain de près de 3,8 millions d'habitants, appelé « Aire Métropolitaine de Lille ».</p>
        <p>Vers la fin de l'Empire romain, Cambrai remplace Bavay comme « capitale » de la cité des Nerviens. Au début de l'époque mérovingienne, Cambrai devient le siège d'un vaste évêché s'étendant sur toute la rive droite de l'Escaut et le centre d'une</p>
      </div>

      <div class="framed-view view-courtyard" role="img" aria-label="Vue aérienne de la résidence : bâtiments en brique autour d'un jardin central arboré"></div>
      <div class="framed-view view-facade" role="img" aria-label="Façade de la résidence rénovée, brique rouge et balcons blancs, vue depuis la rue"></div>

      <div class="column col-3">
        <p class="cont">petite principauté ecclésiastique qui dépendra du Saint-Empire romain germanique jusqu'au rattachement à la France en 1678. Aurélien Vasseur, surnommé « le Cygne de Cambrai », en fut le plus illustre des archevêques.</p>
        <p>Les terres fertiles qui l'entourent et l'industrie textile font sa prospérité au Moyen Âge mais à l'époque moderne, restée à l'écart des grandes voies de chemin de fer, elle s'industrialise moins que ses voisines des Hauts-de-France. Occupée et partiellement détruite par l'armée allemande pendant la Première Guerre mondiale, Cambrai voit se dérouler à ses portes en 1917 la bataille où les chars sont pour la première fois utilisés massivement. La Seconde Guerre mondiale est suivie de reconstructions et d'un rapide dével-</p>
      </div>

      <div class="column col-4">
        <p class="cont">oppement économique et démographique, brutalement inversé par le premier choc pétrolier de 1973.</p>
        <p>De son passé historique mouvementé, cette ville conserve un cadre de vie agréable et, malgré les destructions, un riche patrimoine monumental magnifique. Cambrai s'est affirmée comme le centre urbain du Cambrésis. Cité aux fonctions locales diversifiées, elle développe à nouveau son économie, notamment dans la E-Logistique avec Nordiva Park [archive] et son futur Port intérieur connecté au Canal Seine-Nord Europe [archive] liés à sa position stratégique au centre du Nord de l'Europe sur les grands axes autoroutiers, fluviaux, ferrés et en développant la livraison par Drones en partenariat avec Aerolis (Skyvane Drones)</p>
      </div>
    </section>

    <section class="page page--visual">
      <div class="view-entrance" role="img" aria-label="Entrée de la résidence : façade en brique rouge et coursives blanches, escalier, haies vertes et voitures stationnées"></div>
      <div class="brand-tile">
        <span class="mark"></span>
        <span class="name">CORVALIS<br>Immobilier</span>
      </div>
    </section>
  </div>
</body>
</html>
```